Business Card Design for Portrait photography professional

We are a small company specializing in portrait photography (weddings, family, couples, children, newborn, pregnant, etc.) Occasionally we do business portraits too and do some other type of photography. We need a business card which would fit into the same look and feel as our website theme (lumvika.com - under construction currently).
Our target customer base lies within mid- to upmarket. We want our business cards to convey a feeling of quality, solidness and a bit luxury.
Design should be universal and usable on 85mmx55mm, 90mmx50mm and 90mmx55mm
one extra file (PSD of a website didn't fit into the allowed updoad, therefore has put it into my filecrate: https://www.filecrate-example.net/s/qt7wk2rbvx9dmhe/website%20theme%20PSD.psd)

Target Market(s)

mostly private people, 25-60 years old, mostly well established.

Industry/Entity Type

Portrait Photography

Requirements
Must have
• 2 sided design (print on both sides of the business card).
Must include:
business name, logo, URL (lumvika.no) , employee name, email address, and phone number.
Colorscheme of the website lumvika.no / lumvika.com

```html
<!DOCTYPE html>
<html lang="en">
<head>
<meta charset="utf-8">
<title>lumvika business card</title>
<link rel="stylesheet" href="https://fonts.googleapis.com/css2?family=Source+Sans+3:wght@400;600;700&display=swap">
<style>
  :root {
    --backdrop: #dddce4;
    --card: #f2f0ea;
    --ink-dark: #2b2a27;
    --ink-text: #333230;
    --accent-blue: #c3e0ec;
    --white: #ffffff;
  }
  * { margin: 0; padding: 0; box-sizing: border-box; }
  html, body {
    width: 1200px; height: 987px; overflow: hidden;
    background: var(--backdrop);
    font-family: "Source Sans 3", "Myriad Pro", sans-serif;
  }
  .stage {
    width: 1200px; height: 987px;
    display: flex; align-items: center; justify-content: center; gap: 40px;
  }
  .card {
    position: relative;
    width: 540px; height: 330px;
    background: var(--card);
    border-radius: 22px;
    overflow: hidden;
    box-shadow: 0 4px 14px rgba(40, 40, 60, 0.18);
  }
  .card-front__shapes { position: absolute; inset: 0; }
  .brand-badge {
    position: absolute; left: 50px; top: 18px;
    width: 128px; height: 128px;
    border: 3px solid var(--white); border-radius: 50%;
    display: flex; align-items: center; justify-content: center;
    color: var(--white); font-size: 26px; font-weight: 600; letter-spacing: 1px;
  }
  .employee {
    position: absolute; right: 44px; top: 92px; text-align: right;
    color: var(--white);
  }
  .employee__name { font-size: 25px; font-weight: 700; line-height: 1.1; }
  .employee__title { font-size: 17px; font-weight: 400; margin-top: 2px; }
  .contact {
    position: absolute; right: 44px; bottom: 16px;
    list-style: none; text-align: right; color: var(--ink-text);
    font-size: 20px; line-height: 1.35;
  }
  .contact__item { display: flex; align-items: center; justify-content: flex-end; gap: 8px; }
  .contact__icon { width: 16px; height: 16px; }
  .card-back {
    display: flex; flex-direction: column; align-items: center; justify-content: center;
  }
  .back-mark {
    width: 160px; height: 160px;
    border: 2px solid var(--ink-dark); border-radius: 50%;
    display: flex; align-items: center; justify-content: center;
    color: var(--ink-dark); font-size: 30px; font-weight: 600; letter-spacing: 1px;
  }
  .back-url {
    margin-top: 20px; color: var(--ink-text);
    font-size: 18px; letter-spacing: 5px;
  }
</style>
</head>
<body>
<main class="stage">
  <section class="card card-front">
    <svg class="card-front__shapes" viewBox="0 0 540 330" width="540" height="330" aria-hidden="true">
      <path d="M0,162 Q300,236 540,212 L540,207 Q300,228 0,155 Z" fill="var(--accent-blue)"/>
      <path d="M0,155 Q300,228 540,207 L540,204.5 Q300,224 0,152.5 Z" fill="var(--ink-dark)"/>
      <path d="M0,0 H540 V200 Q300,215 0,148 Z" fill="var(--ink-dark)"/>
    </svg>
    <div class="brand-badge">lumvika</div>
    <div class="employee">
      <p class="employee__name">employee name</p>
      <p class="employee__title">Title</p>
    </div>
    <ul class="contact">
      <li class="contact__item">
        <svg class="contact__icon" viewBox="0 0 16 16" aria-hidden="true"><circle cx="8" cy="8" r="7.5" fill="var(--ink-text)"/><path d="M5.2 4.2l1.4 1.6-.8 1c.6 1.2 1.4 2 2.5 2.5l1-.8 1.6 1.4-.9 1.3C7.6 11 5 8.4 4.3 5.1z" fill="var(--card)"/></svg>
        <span>123-555-0142</span>
      </li>
      <li class="contact__item">
        <svg class="contact__icon" viewBox="0 0 16 16" aria-hidden="true"><rect x="1" y="3.5" width="14" height="9.5" rx="1" fill="var(--ink-text)"/><path d="M1.5 4.2L8 9l6.5-4.8" stroke="var(--card)" stroke-width="1.2" fill="none"/></svg>
        <span>info@lumvika.com</span>
      </li>
      <li class="contact__item">
        <svg class="contact__icon" viewBox="0 0 16 16" aria-hidden="true"><g fill="none" stroke="var(--ink-text)" stroke-width="1.2"><circle cx="8" cy="8" r="7"/><ellipse cx="8" cy="8" rx="3" ry="7"/><path d="M1 8h14M2.2 4.5h11.6M2.2 11.5h11.6"/></g></svg>
        <span>www.lumvika.com</span>
      </li>
    </ul>
  </section>

  <section class="card card-back">
    <div class="back-mark">lumvika</div>
    <p class="back-url">www.lumvika.com</p>
  </section>
</main>
</body>
</html>
```